Poster for a 100 y.o. Tennis Tournament

I would like a poster designed to promote our tennis tournament but I'd like to avoid some of the clichés like the shadow of a player serving. Just well styled text would be fine but some clever imagery would be a bonus.
Highlighting the fact our tournament has been running for over 100 years would be nice so a retro design would work. But that doesn't mean a modern design, for example a minimalist approach utilising the lines of a tennis court, wouldn't work.
Updates

Our tennis committee is now in the process of short listing and will provide an update within 48 hours.

Industry/Entity Type

Court

Requirements
Must have
• The poster must contain the following text at a minimum:
"Marbury Tennis Tournament"/"Since 1908"
"9 March - 11 March, 2013" or "9-11 March, 2013", etc
"www.marburytennis.com.au"

The poster must be reproducible in colour and black & white, or at least have an alternate for black & white.

The poster must be usable in both A3 and A4 sizes.
Nice to have
• The poster should contain the following text:
"Championship"
"Handicap"
"Seniors"
"Juniors"
Each above may be optionally succeeded by "Singles & Doubles", e.g. "Championship Singles & Doubles". It would actually be clearer if this additional text was used but would be repetitive, so alternate text "Singles & Doubles in all categories" might also be used. Alternatives for variety (with the first word the focus): "Championship Singles & Doubles", "Handicap Singles & Doubles", "Seniors 35+ & 50+", "Juniors 18&U, 14&U"

Ideally the poster will provision room for four to eight sponsors logos, preferably at the bottom, but failure to do this is not a show stopper.

The following text may also be used:
"Entries close February 24"
"Tollard Plate Weekend"

Attached is a photo of one of the old trophies. Utilisation of the curved style of the "Marbury Tennis Tournament" text would fit in with the history if the tournament.

The ability to reuse elements of the poster in a single page website used to promote the tournament would be an advantage (as it will provide consistency).

If you could have an image of a tennis ball that conveys the same energy as the clock/tyre image in the attached "Under the Glass Moon" poster, that would be cool. Or using split imagery of a wooden racquet and a modern racquet, but with some energy, would also be good. These are just ideas though and by no means essential.

I've also attached a photo of a t-shirt with a poster layout I thought looked good.

Some additional text that can be used:
"Brand new courts"
"Brindle Park, Oakhurst Tce, Marbury"
"Phone 0427 318 642"
"Prizes and Trophies"

```html
<!DOCTYPE html>
<html lang="en">
<head>
<meta charset="utf-8">
<title>Marbury Tennis Tournament – Poster Options</title>
<link rel="stylesheet" href="https://fonts.googleapis.com/css2?family=Alfa+Slab+One&family=Encode+Sans+Condensed:wght@500;700&family=Oswald:wght@700&display=swap">
<style>
  :root {
    --paper: #ffffff;
    --sage: #c2cfa6;
    --sage-light: #dce4c6;
    --sage-dark: #9fb086;
    --ink: #0d0d0d;
    --crimson: #7d1111;
    --band-text: #ffffff;
  }
  * { margin: 0; padding: 0; box-sizing: border-box; }
  html, body { width: 1200px; height: 827px; overflow: hidden; background: var(--paper); }
  body { position: relative; font-family: "Encode Sans Condensed", "Arial Narrow", sans-serif; }

  .poster {
    position: absolute;
    top: 5px;
    height: 812px;
    overflow: hidden;
    background: var(--sage);
  }
  .poster--arched { left: 5px; width: 590px; }
  .poster--stacked { left: 612px; width: 583px; }

  .poster__texture {
    position: absolute; inset: 0;
    background:
      radial-gradient(ellipse at 55% 60%, var(--sage-light) 0%, transparent 55%),
      linear-gradient(180deg, var(--sage-dark) 0%, var(--sage) 30%, var(--sage-light) 75%, var(--sage) 100%);
  }
  .poster__edge-top { position: absolute; left: 0; top: 0; width: 100%; height: 20px; background: var(--ink); }
  .poster__edge-left { position: absolute; left: 0; top: 0; width: 30px; height: 300px; background: var(--ink); }

  .poster__title { position: absolute; left: 0; top: 0; width: 100%; height: 340px; }
  .title-arched { font-family: "Oswald", "Arial Narrow", sans-serif; font-weight: 700; font-size: 40px; fill: var(--crimson); stroke: var(--ink); stroke-width: 1.4px; }
  .title-stacked { font-family: "Alfa Slab One", Georgia, serif; fill: var(--crimson); stroke: var(--ink); stroke-width: 1.4px; }

  .poster__date {
    position: absolute; width: 100%; text-align: center;
    font-weight: 700; font-size: 46px; color: var(--ink); letter-spacing: 0.5px;
  }
  .poster__since { position: absolute; font-size: 26px; color: var(--ink); }

  .events { position: absolute; list-style: none; }
  .events li { font-size: 44px; line-height: 1; color: var(--crimson); font-weight: 500; }

  .events-note {
    position: absolute; width: 300px; text-align: center;
    font-size: 34px; line-height: 1.05; color: var(--ink);
    transform: rotate(-13deg);
  }
  .entries {
    position: absolute; width: 420px; text-align: center;
    font-size: 28px; line-height: 1.3; color: var(--ink);
  }
  .poster__footer {
    position: absolute; left: 0; bottom: 0; width: 100%;
    background: var(--ink); color: var(--band-text);
    text-align: center; font-size: 40px; letter-spacing: 0.5px;
  }
</style>
</head>
<body>

<section class="poster poster--arched">
  <div class="poster__texture" role="img" aria-label="Weathered sage-green grunge backdrop with faint embossed tennis players and red paint spatter"></div>
  <div class="poster__edge-top"></div>
  <div class="poster__edge-left"></div>

  <svg class="poster__title" viewBox="0 0 590 340" aria-label="Marbury Tennis Tournament">
    <defs><path id="arc-arched" d="M 40 200 Q 300 40 575 190"/></defs>
    <text class="title-arched"><textPath href="#arc-arched" startOffset="50%" text-anchor="middle" textLength="540" lengthAdjust="spacingAndGlyphs">MARBURY TENNIS TOURNAMENT</textPath></text>
  </svg>

  <p class="poster__date" style="top:240px;">9 March – 11 March &nbsp;2013</p>
  <p class="poster__since" style="top:312px; right:24px;">*Since 1908</p>

  <ul class="events" style="left:20px; top:372px;">
    <li style="margin-bottom:22px;">Championship</li>
    <li style="margin-bottom:20px;">Handicap</li>
    <li style="margin-bottom:22px;">Seniors</li>
    <li>Juniors</li>
  </ul>
  <p class="events-note" style="left:285px; top:440px;">Singles &amp;<br>Doubles<br>in all categories</p>

  <p class="entries" style="left:90px; top:644px;">Entries close February 24<br>Tollard Plate Weekend</p>

  <footer class="poster__footer" style="height:67px; line-height:67px;">www.marburytennis.com.au</footer>
</section>

<section class="poster poster--stacked">
  <div class="poster__texture" role="img" aria-label="Weathered sage-green grunge backdrop with faint embossed tennis players and red paint spatter"></div>
  <div class="poster__edge-top"></div>
  <div class="poster__edge-left"></div>

  <svg class="poster__title" viewBox="0 0 583 340" aria-label="Marbury Tennis Tournament">
    <defs>
      <path id="arc-line-one" d="M 40 160 Q 290 40 550 175"/>
      <path id="arc-line-two" d="M 80 275 Q 300 250 540 290"/>
    </defs>
    <text class="title-stacked" font-size="46"><textPath href="#arc-line-one" startOffset="50%" text-anchor="middle" textLength="500" lengthAdjust="spacingAndGlyphs">MARBURY TENNIS</textPath></text>
    <text class="title-stacked" font-size="52"><textPath href="#arc-line-two" startOffset="50%" text-anchor="middle" textLength="440" lengthAdjust="spacingAndGlyphs">TOURNAMENT</textPath></text>
  </svg>

  <p class="poster__since" style="top:302px; right:12px;">*Since 1908</p>
  <p class="poster__date" style="top:346px;">9 March – 11 March &nbsp;2013</p>

  <ul class="events" style="left:28px; top:418px;">
    <li style="margin-bottom:25px;">Championship</li>
    <li style="margin-bottom:16px;">Handicap</li>
    <li style="margin-bottom:21px;">Seniors</li>
    <li>Juniors</li>
  </ul>
  <p class="events-note" style="left:290px; top:470px;">Singles &amp;<br>Doubles<br>in all categories</p>

  <p class="entries" style="left:83px; top:662px;">Entries close February 24<br>Tollard Plate Weekend</p>

  <footer class="poster__footer" style="height:60px; line-height:60px;">www.marburytennis.com.au</footer>
</section>

</body>
</html>
```